Letterhead Design

We need a new Letterhead design for a 30 year old Electrical Company. We service domestic and commercial places. We have a logo recently made so to incorporate that. Using same colours or interested to see others added.
Would like to see a couple of options with all the info in letterhead, then another with info in a footnote down the bottom.

info needed to be added:

-Lic. No 48162
8/22-24 Larkin Rd, Tolvern 2087
W - brightcoilpower.com.au
T - (02) 9471 3825
M - 0427 593 168
E - info@brightcoilpower.com.au
ABN: 42 597 214 630

Electrical

```html
<!DOCTYPE html>
<html lang="en">
<head>
<meta charset="utf-8">
<title>Brightcoil Power – Letterhead</title>
<link href="https://fonts.googleapis.com/css2?family=Open+Sans:wght@400;600;700&display=swap" rel="stylesheet">
<style>
  :root {
    --orange: #f7941d;
    --peach: #fde3c8;
    --ink: #0b0b0b;
    --paper: #ffffff;
    --footer-text: #f2f2f2;
    --divider: #3a3a3a;
  }
  * { box-sizing: border-box; margin: 0; padding: 0; }
  html, body { width: 848px; height: 1200px; overflow: hidden; background: var(--paper); }
  body { font-family: "Open Sans", Arial, sans-serif; }

  .letterhead { position: relative; width: 848px; height: 1200px; background: var(--paper); }

  .top-bar { position: absolute; left: 0; top: 0; width: 100%; height: 17px; background: var(--orange); }
  .top-band { position: absolute; left: 0; top: 17px; width: 100%; height: 61px; background: var(--peach); }

  .brand-plate {
    position: absolute; left: 27px; top: 30px; width: 247px; height: 93px;
    background: var(--paper);
    display: flex; align-items: center; justify-content: center;
  }
  .brand-name {
    font-size: 25px; font-weight: 700; color: var(--ink); letter-spacing: 0.5px;
  }

  .footer {
    position: absolute; left: 0; bottom: 0; width: 100%; height: 56px;
    background: var(--ink); color: var(--footer-text);
  }
  .footer-abn {
    position: absolute; left: 0; top: 0; width: 136px; height: 56px;
    background: var(--orange); color: var(--ink);
    font-size: 11px; font-weight: 600;
    display: flex; align-items: center; padding-left: 18px;
  }
  .footer-item { position: absolute; top: 0; height: 56px; display: flex; align-items: center; }
  .footer-icon {
    width: 27px; height: 27px; background: var(--orange);
    display: flex; align-items: center; justify-content: center; margin-right: 9px;
  }
  .footer-icon svg { width: 19px; height: 19px; }
  .footer-lines { font-size: 10.2px; line-height: 14px; white-space: nowrap; }
  .footer-lines b { font-weight: 700; }
  .item-address { left: 168px; }
  .item-web { left: 407px; }
  .item-phone { left: 638px; }
  .footer-divider { position: absolute; top: 9px; width: 1px; height: 36px; background: var(--divider); }
  .divider-one { left: 393px; }
  .divider-two { left: 631px; }
</style>
</head>
<body>
<main class="letterhead">
  <div class="top-bar"></div>
  <div class="top-band"></div>

  <header class="brand-plate">
    <span class="brand-name">Brightcoil Power</span>
  </header>

  <footer class="footer">
    <div class="footer-abn">ABN: 42 597 214 630</div>

    <div class="footer-item item-address">
      <div class="footer-icon">
        <svg viewBox="0 0 24 24" aria-hidden="true"><path fill="#0b0b0b" d="M12 2a7 7 0 0 0-7 7c0 5.2 7 13 7 13s7-7.8 7-13a7 7 0 0 0-7-7zm0 9.6A2.6 2.6 0 1 1 12 6.4a2.6 2.6 0 0 1 0 5.2z"/></svg>
      </div>
      <div class="footer-lines">-Lic. No 48162<br>8/22-24 Larkin Rd, Tolvern 2087</div>
    </div>

    <div class="footer-divider divider-one"></div>

    <div class="footer-item item-web">
      <div class="footer-icon">
        <svg viewBox="0 0 24 24" aria-hidden="true" fill="none" stroke="#0b0b0b" stroke-width="1.8"><circle cx="12" cy="12" r="9"/><ellipse cx="12" cy="12" rx="4" ry="9"/><path d="M3 12h18M5 7h14M5 17h14"/></svg>
      </div>
      <div class="footer-lines">W - brightcoilpower.com.au<br>E &nbsp;- info@brightcoilpower.com.au</div>
    </div>

    <div class="footer-divider divider-two"></div>

    <div class="footer-item item-phone">
      <div class="footer-icon">
        <svg viewBox="0 0 24 24" aria-hidden="true"><path fill="#0b0b0b" d="M6.6 10.8a15.1 15.1 0 0 0 6.6 6.6l2.2-2.2a1 1 0 0 1 1-.25 11.4 11.4 0 0 0 3.6.57 1 1 0 0 1 1 1V20a1 1 0 0 1-1 1A17 17 0 0 1 3 4a1 1 0 0 1 1-1h3.5a1 1 0 0 1 1 1c0 1.25.2 2.45.57 3.57a1 1 0 0 1-.25 1z"/></svg>
      </div>
      <div class="footer-lines">T &nbsp;- (02) <b>9471 3825</b><br>M - 0427 <b>593 168</b></div>
    </div>
  </footer>
</main>
</body>
</html>
```